Tallow Brook Website - Sell Outdoor product

We are a mom and pop company that just opened our website.

We need a fresh, professional, and nice looking website for our outdoor products. We sell hunting, camping, fishing, and hiking products/accessories to name a few. Some of these products are optics, gun safes, gun bi-pods and tripods, gun lights, hunting camera, tents, hearing protection, targets, fishing poles, and hiking backpacks to name a few.

Our current website is: http://www.tallowbrook.example . You'll see our logo on the website, and it is attached. We aren't married to this logo, so if the designer thinks they can modify it or even come up with a better design for the website, they are more than welcome to do so. We need someone with good images of their own (clip art and/or outdoor images) they can use if they need to for our website.

I also attached a idea I had in visio, but please don't think this is set in stone. It is just a very rough idea. You can also go to our zintaro site to see what we sell: www.zintaro.example/shops/q7xk402mdrvp3s . Right now we sell everything on Zintaro, but our website will just focus on outdoor product. So please make it an outdoor focused website. And you can be creative with some of the product category names. We also want to leave room for some parallel product in the future. Like garden tools, back yard furniture, and BBQs.

Our company also wants to include a deals section on the website. We will probably update it once a week or month. I have included what I did for a deal and accompanying images for it. Image is called Morvelki (And the main images are 01 and 02).

We also want to make sure the file is compatible with our current web-hosting company, https://www.shelvora.example. So I included a webpage layout zip folder. If you have any questions, please contact me.

This is for a PSD and HTML/CSS webpage. If you have any artwork or images that you own and want to use them for the webpage, please do so.

Target Market(s)

The hunter, outdoors person, camper, hiker, and etc.

Industry/Entity Type

It Company

Coding

Coded - Design and coding required

Number of Pages Required

3 page

Requirements
Must have
• The main page. PSD and HTML/CSS file.
• The category page. PSD and HTML/CSS file
• The product display page. PSD and HTML/CSS file
• Please also use some images that you have or from the sites below:
• You can get free stock images for 7 days (20 per day) from this site:
• https://www.pixelbarn.example/complimentary/KTRPLQX/?utm_source=KTRPLQFreeX&utm_medium=cpc&utm_campaign=KTRPLQFreeX&gclid=ZXPq8rTmwnB4DHuLoPeaWs2kTb
• Has 14 good sites:
• http://www.ventureledger.example/article/519372
• Here are the ones I like:
• https://clearpane.example/
• http://grandolim.example/
• http://www.sitewright.example/free/nature
• http://www.dustvault.example/archive
• http://tinyframes.example/
• http://olq.brvkmt.example/search/hiking
• http://fetchqovi.blogspin.example/
• http://roelvastor.example/post/584930271164/download
• http://openvaultlibrary.example/
• If there is a photographer listed on or next to the image, on the bottom lower corner of the image, please put the photographer's name.
Nice to have
• I would like to have an unsubscribe page. If the designer has any of their own images of the outdoor world, and they want to use them, please do. Just make the right graphic changes to make it look good.
Should not have
• Try and keep green color to a minimum.

```html
<!DOCTYPE html>
<html lang="en">
<head>
<meta charset="utf-8">
<title>Tallow Brook – Outdoor Store</title>
<link rel="stylesheet" href="https://fonts.googleapis.com/css2?family=Open+Sans:wght@400;600;700&family=Raleway:wght@600;700;800&display=swap">
<style>
:root{
  --accent:#e2b317;
  --accent-dark:#c99c0c;
  --ink:#1b1b1b;
  --text:#555;
  --muted:#8a8a8a;
  --line:#e3e3e3;
  --band:#efefef;
  --footer:#141414;
  --footer-text:#9a9a9a;
  --white:#fff;
  --sky:#dfe7ec;
  --sea:#3f6d86;
  --sea-deep:#2b4f66;
  --rock:#5a4c40;
  --rock-dark:#2e2620;
  --case:#2a2a2a;
  --brass:#b8903a;
}
*{box-sizing:border-box;margin:0;padding:0}
html,body{width:1200px;height:2340px;overflow:hidden;background:var(--white)}
body{font-family:"Open Sans",Arial,sans-serif;color:var(--text);font-size:13px;position:relative}
ul{list-style:none}

/* Header */
.site-header{height:96px;position:relative}
.support{position:absolute;left:140px;top:40px;font-size:10px;letter-spacing:.5px;color:var(--muted);text-transform:uppercase}
.brand{position:absolute;left:50%;top:24px;transform:translateX(-50%);display:flex;align-items:center;gap:10px}
.brand-mark{width:22px;height:22px;background:var(--accent)}
.brand-name{font-family:"Raleway",Arial,sans-serif;font-weight:800;font-size:30px;color:var(--ink)}
.header-tools{position:absolute;right:140px;top:34px;display:flex;align-items:center;gap:34px}
.search-btn{width:26px;height:26px;border-radius:50%;background:#e9e9e9;display:flex;align-items:center;justify-content:center}
.cart{display:flex;align-items:center;gap:8px;font-size:12px;color:var(--ink)}

/* Navigation */
.main-nav{height:48px;border-top:1px solid var(--line);border-bottom:1px solid var(--line)}
.main-nav ul{display:flex;justify-content:center;gap:38px;height:100%;align-items:center}
.main-nav a{font-family:"Raleway",Arial,sans-serif;font-weight:700;font-size:11px;letter-spacing:.6px;color:var(--ink);text-decoration:none;text-transform:uppercase;padding:15px 0;border-bottom:3px solid transparent}
.main-nav a.is-active{color:var(--accent);border-bottom-color:var(--accent)}

/* Hero */
.hero{height:408px;background:
  linear-gradient(100deg,rgba(90,76,64,0) 0%,rgba(90,76,64,0) 52%,rgba(74,62,52,.85) 66%,rgba(46,38,32,.95) 100%),
  linear-gradient(180deg,var(--sky) 0%,#cfdbe3 18%,#8fa9b9 26%,var(--sea) 36%,var(--sea-deep) 50%,var(--rock) 62%,#443a31 80%,var(--rock-dark) 100%)}

/* Products */
.new-products{padding-top:32px}
.section-title{font-family:"Raleway",Arial,sans-serif;font-weight:700;font-size:17px;color:var(--accent);text-align:center;letter-spacing:1px;text-transform:uppercase}
.product-grid{width:920px;margin:20px auto 0;display:grid;grid-template-columns:repeat(4,200px);column-gap:40px;row-gap:22px}
.product-card{text-align:center;height:358px}
.product-media{height:216px;border:1px solid var(--line);padding:10px;background:var(--white)}
.product-photo{width:100%;height:100%}
.photo-case{background:radial-gradient(ellipse 62% 38% at 50% 52%,#4a4a4a 0%,var(--case) 55%,#8c8c8c 78%,#f4f4f4 100%)}
.photo-round{background:linear-gradient(135deg,#f6f6f6 0%,#ececec 30%,#d2b77a 44%,var(--brass) 50%,#3a3a3a 58%,#cfcfcf 72%,#f6f6f6 100%)}
.product-title{margin-top:22px;font-family:"Raleway",Arial,sans-serif;font-weight:700;font-size:11px;line-height:15px;letter-spacing:.4px;color:var(--accent);text-transform:uppercase}
.product-price{margin-top:14px;font-family:"Raleway",Arial,sans-serif;font-weight:800;font-size:18px;color:var(--ink)}
.add-to-cart{margin-top:10px;display:inline-block;border:1px solid #cfcfcf;background:var(--white);font-size:9px;font-weight:700;letter-spacing:.4px;color:var(--ink);padding:7px 16px}

/* Newsletter */
.newsletter{position:absolute;left:140px;top:1420px;width:920px;height:240px;background:var(--band);padding:34px}
.newsletter-box{background:var(--white);height:172px;display:flex;align-items:center;justify-content:space-between;padding:0 36px}
.newsletter h3{font-family:"Raleway",Arial,sans-serif;font-weight:800;font-size:14px;color:var(--ink);text-transform:uppercase;margin-bottom:10px}
.newsletter p{width:400px;font-size:11px;line-height:17px;color:var(--muted)}
.signup{display:flex}
.signup-field{width:300px;height:38px;border:1px solid var(--line);font-size:11px;color:#aaa;padding:11px 14px}
.signup-btn{width:96px;height:38px;background:var(--accent);color:var(--white);font-size:10px;font-weight:700;letter-spacing:.6px;display:flex;align-items:center;justify-content:center}

/* Info columns */
.info-row{position:absolute;left:140px;top:1700px;width:920px;display:flex;justify-content:space-between}
.info-col{width:280px}
.info-col h4{font-family:"Raleway",Arial,sans-serif;font-weight:800;font-size:13px;color:var(--ink);text-transform:uppercase;padding-bottom:12px;border-bottom:1px solid var(--line);margin-bottom:20px}
.promo-media{width:200px;height:176px;margin:0 auto 18px;border:1px solid var(--line);background:linear-gradient(150deg,#ffffff 0%,#faf7ee 40%,#e9d9a8 62%,var(--brass) 78%,#2c2c2c 100%)}
.info-col p{font-size:11px;line-height:18px;color:var(--muted)}
.address-card{background:#f4f4f4;padding:18px 20px;height:250px}
.address-card h5{font-size:11px;font-weight:700;color:var(--ink);letter-spacing:.5px;margin-bottom:16px}
.address-card li{display:flex;align-items:flex-start;gap:10px;font-size:11px;line-height:16px;color:var(--muted);margin-bottom:16px}
.address-card svg{flex:0 0 14px;margin-top:1px}
.feature-list{margin-top:20px}
.feature-list li{display:flex;align-items:center;gap:12px;font-size:11px;color:var(--muted);padding:12px 0;border-bottom:1px solid var(--line)}
.feature-list li::before{content:"";width:7px;height:7px;border-radius:50%;background:var(--accent)}

/* Footer */
.site-footer{position:absolute;left:0;top:2080px;width:1200px;height:260px;background:var(--footer);color:var(--footer-text)}
.footer-cols{position:absolute;left:140px;top:40px;display:flex}
.footer-col{width:262px}
.footer-col h4{font-family:"Raleway",Arial,sans-serif;font-weight:800;font-size:13px;color:var(--white);text-transform:uppercase;margin-bottom:14px}
.footer-col li{font-size:10px;line-height:20px}
.footer-bottom{position:absolute;left:140px;right:140px;bottom:28px;display:flex;justify-content:space-between;align-items:center;border-top:1px solid #2a2a2a;padding-top:18px;font-size:10px}
.social{display:flex;gap:8px}
.social span{width:16px;height:16px;border-radius:50%;background:var(--accent)}
</style>
</head>
<body>

<header class="site-header">
  <div class="support">Support: +1 555 0142-0187</div>
  <div class="brand">
    <span class="brand-mark"></span>
    <span class="brand-name">Tallow Brook</span>
  </div>
  <div class="header-tools">
    <span class="search-btn">
      <svg width="12" height="12" viewBox="0 0 12 12"><circle cx="5" cy="5" r="3.6" fill="none" stroke="#777" stroke-width="1.4"/><line x1="7.7" y1="7.7" x2="11" y2="11" stroke="#777" stroke-width="1.4"/></svg>
    </span>
    <span class="cart">
      <svg width="18" height="16" viewBox="0 0 18 16"><path d="M1 1h3l2 9h9l2-6H5" fill="none" stroke="#1b1b1b" stroke-width="1.4"/><circle cx="7" cy="14" r="1.3" fill="#1b1b1b"/><circle cx="14" cy="14" r="1.3" fill="#1b1b1b"/></svg>
      <span>Cart: $0.00</span>
    </span>
  </div>
</header>

<nav class="main-nav">
  <ul>
    <li><a class="is-active">Binoculars</a></li>
    <li><a>Metal Detectors</a></li>
    <li><a>Microscopes</a></li>
    <li><a>Riflescopes</a></li>
    <li><a>Safe</a></li>
    <li><a>Shooting Accessories</a></li>
    <li><a>Spotting Scopes</a></li>
    <li><a>Telescopes</a></li>
  </ul>
</nav>

<div class="hero" role="img" aria-label="Photo of a rocky coastline meeting blue sea under a pale sky"></div>

<section class="new-products">
  <h2 class="section-title">New Products</h2>
  <div class="product-grid">
    <article class="product-card">
      <div class="product-media"><div class="product-photo photo-case" role="img" aria-label="Photo of a black portable solar charger case"></div></div>
      <h3 class="product-title">Portable Solar Charger<br>Case with Speaker</h3>
      <div class="product-price">$60.68</div>
      <span class="add-to-cart">ADD TO CART</span>
    </article>
    <article class="product-card">
      <div class="product-media"><div class="product-photo photo-round" role="img" aria-label="Photo of a brass rifle cartridge gift item"></div></div>
      <h3 class="product-title">Portable Solar Charger<br>Case with Speaker</h3>
      <div class="product-price">$60.68</div>
      <span class="add-to-cart">ADD TO CART</span>
    </article>
    <article class="product-card">
      <div class="product-media"><div class="product-photo photo-round" role="img" aria-label="Photo of a brass rifle cartridge gift item"></div></div>
      <h3 class="product-title">Portable Solar Charger<br>Case with Speaker</h3>
      <div class="product-price">$60.68</div>
      <span class="add-to-cart">ADD TO CART</span>
    </article>
    <article class="product-card">
      <div class="product-media"><div class="product-photo photo-case" role="img" aria-label="Photo of a black portable solar charger case"></div></div>
      <h3 class="product-title">Portable Solar Charger<br>Case with Speaker</h3>
      <div class="product-price">$60.68</div>
      <span class="add-to-cart">ADD TO CART</span>
    </article>
    <article class="product-card">
      <div class="product-media"><div class="product-photo photo-case" role="img" aria-label="Photo of a black portable solar charger case"></div></div>
      <h3 class="product-title">Portable Solar Charger<br>Case with Speaker</h3>
      <div class="product-price">$60.68</div>
      <span class="add-to-cart">ADD TO CART</span>
    </article>
    <article class="product-card">
      <div class="product-media"><div class="product-photo photo-round" role="img" aria-label="Photo of a brass rifle cartridge gift item"></div></div>
      <h3 class="product-title">Portable Solar Charger<br>Case with Speaker</h3>
      <div class="product-price">$60.68</div>
      <span class="add-to-cart">ADD TO CART</span>
    </article>
    <article class="product-card">
      <div class="product-media"><div class="product-photo photo-round" role="img" aria-label="Photo of a brass rifle cartridge gift item"></div></div>
      <h3 class="product-title">Portable Solar Charger<br>Case with Speaker</h3>
      <div class="product-price">$60.68</div>
      <span class="add-to-cart">ADD TO CART</span>
    </article>
    <article class="product-card">
      <div class="product-media"><div class="product-photo photo-case" role="img" aria-label="Photo of a black portable solar charger case"></div></div>
      <h3 class="product-title">Portable Solar Charger<br>Case with Speaker</h3>
      <div class="product-price">$60.68</div>
      <span class="add-to-cart">ADD TO CART</span>
    </article>
  </div>
</section>

<section class="newsletter">
  <div class="newsletter-box">
    <div>
      <h3>Stay tuned and up to date!</h3>
      <p>Stay informed about new arrivals, weekly deals and seasonal gear picks for your next trip outdoors.</p>
    </div>
    <div class="signup">
      <div class="signup-field">Your email address</div>
      <div class="signup-btn">SUBSCRIBE</div>
    </div>
  </div>
</section>

<section class="info-row">
  <div class="info-col">
    <h4>Product Services</h4>
    <div class="promo-media" role="img" aria-label="Deal promotion showing a cartridge shaped bottle opener"></div>
    <p>Solid brass bottle openers shaped like rifle rounds make a great gift for any hunter at camp.</p>
  </div>
  <div class="info-col">
    <h4>Company Address</h4>
    <div class="address-card">
      <h5>INFORMATION</h5>
      <ul>
        <li><svg width="14" height="14" viewBox="0 0 14 14"><path d="M7 1a4 4 0 0 0-4 4c0 3 4 8 4 8s4-5 4-8a4 4 0 0 0-4-4z" fill="#e2b317"/><circle cx="7" cy="5" r="1.5" fill="#fff"/></svg>1200 Cedar Ridge Road, Pinehollow, OR 97000</li>
        <li><svg width="14" height="14" viewBox="0 0 14 14"><path d="M3 1l2.5 3-1.5 1.5a8 8 0 0 0 4.5 4.5L10 8.5l3 2.5-1.5 2C6 13 1 8 1 2.5z" fill="#e2b317"/></svg>+1 555 0101-7744</li>
        <li><svg width="14" height="14" viewBox="0 0 14 14"><path d="M3 1l2.5 3-1.5 1.5a8 8 0 0 0 4.5 4.5L10 8.5l3 2.5-1.5 2C6 13 1 8 1 2.5z" fill="#e2b317"/></svg>+1 555 0102-8830</li>
        <li><svg width="14" height="14" viewBox="0 0 14 14"><rect x="1" y="3" width="12" height="8" fill="#e2b317"/><path d="M1 3l6 5 6-5" fill="none" stroke="#fff" stroke-width="1"/></svg>hello@tallowbrook.example</li>
      </ul>
    </div>
  </div>
  <div class="info-col">
    <h4>Aditional Informations</h4>
    <p>Our team tests the gear we sell so you can head out with confidence in every season.</p>
    <ul class="feature-list">
      <li>Free shipping on orders over $99</li>
      <li>Gear checked by our staff</li>
      <li>Easy returns within thirty days</li>
      <li>Weekly deals updated every Monday</li>
    </ul>
  </div>
</section>

<footer class="site-footer">
  <div class="footer-cols">
    <div class="footer-col">
      <h4>Company</h4>
      <ul><li>About us</li><li>Location</li><li>Privacy policy</li><li>Terms &amp; conditions</li></ul>
    </div>
    <div class="footer-col">
      <h4>Customer Services</h4>
      <ul><li>Contact</li><li>Frequently asked questions</li><li>Returns &amp; exchanges</li><li>Service guides</li></ul>
    </div>
    <div class="footer-col">
      <h4>Can we help you?</h4>
      <ul><li>Customer service</li><li>Email: hello@tallowbrook.example</li><li>Phone: +1 555 0101 7744</li></ul>
    </div>
  </div>
  <div class="footer-bottom">
    <span>© 2015 Tallow Brook</span>
    <div class="social"><span></span><span></span><span></span><span></span></div>
  </div>
</footer>

</body>
</html>
```